Brand New Church Business Card Design. Needs to appeal to high school students, professionals.

Business Card. Bold lines and colors. Simple font. This is a new church looking to attract new families who have moved to the area. Business professionals mostly. have a working logo. may need a little tweaking. Church is designed to do excellent ministries for students and children. Like business card design in box on mark vault homepage. Want a front and back side. Prefer colors to match the logo. But will lean on designers preferences and wisdom. DO NOT WANT A CROSS OR RELIGIOUS SYMBOL on the card.

Target Market(s)

Families, Professionals, Students

Industry/Entity Type

High School

Contact Information for Business Card

SaltRock ChurchSaltRock.atForrest Coulter904-515-8349Forrest@PineHollow.at

Font styles to use
Sans Serif

Colors
0255a3
ffffff

Requirements
Must have
• Bold colors. Very Masculine. Creative
Nice to have
• On printnook.markvault.com homepage in the business card design box. the card with the black, blue and gray looks really sharp. matches our logos.
Should not have
• no crosses or religious symbols.

```html
<!DOCTYPE html>
<html lang="en">
<head>
<meta charset="utf-8">
<title>PineHollow Church – Business Card</title>
<link rel="stylesheet" href="https://fonts.googleapis.com/css2?family=Arimo:wght@700&family=Poppins:wght@300&display=swap">
<style>
  :root {
    --brand-blue: #0255a3;
    --brand-blue-bright: #1470b8;
    --card-white: #f3f3f1;
    --card-black: #000000;
    --panel-black: #0b0b0b;
    --ink: #2a2a2a;
    --backdrop: #dcdcdc;
    --on-dark: #ffffff;
  }
  * { box-sizing: border-box; margin: 0; padding: 0; }
  html, body {
    width: 1200px;
    height: 900px;
    overflow: hidden;
    background: var(--backdrop);
  }
  .canvas {
    position: relative;
    width: 1200px;
    height: 900px;
  }
  .card {
    position: absolute;
    top: 307px;
    width: 500px;
    height: 286px;
    box-shadow: 0 6px 18px rgba(0, 0, 0, 0.12);
  }

  /* Back side: contact details */
  .card--back {
    left: 70px;
    background: var(--card-white);
  }
  .card__brand {
    position: absolute;
    left: 34px;
    top: 30px;
    display: flex;
    align-items: center;
    gap: 12px;
  }
  .brand-dot {
    width: 40px;
    height: 40px;
    border-radius: 50%;
    background: var(--brand-blue-bright);
  }
  .brand-name {
    font-family: "Arimo", Arial, sans-serif;
    font-weight: 700;
    font-size: 19px;
    color: var(--brand-blue-bright);
  }
  .contact-list {
    position: absolute;
    left: 190px;
    top: 112px;
    list-style: none;
  }
  .contact-list li {
    display: flex;
    align-items: center;
    gap: 14px;
    height: 42px;
    font-family: "Poppins", Arial, sans-serif;
    font-weight: 300;
    font-size: 15px;
    color: var(--ink);
  }
  .contact-icon {
    width: 15px;
    height: 15px;
    flex: none;
  }

  /* Front side: name mark */
  .card--front {
    left: 630px;
    background: var(--card-black);
  }
  .front-panel {
    position: absolute;
    left: 70px;
    top: 48px;
    width: 360px;
    height: 190px;
    background: var(--panel-black);
    display: flex;
    align-items: center;
    justify-content: center;
    gap: 18px;
  }
  .front-dot {
    width: 110px;
    height: 110px;
    border-radius: 50%;
    background: var(--brand-blue-bright);
  }
  .front-name {
    font-family: "Arimo", Arial, sans-serif;
    font-weight: 700;
    font-size: 27px;
    line-height: 1.1;
    color: var(--on-dark);
  }
</style>
</head>
<body>
<main class="canvas">

  <section class="card card--back" aria-label="Card back">
    <div class="card__brand">
      <span class="brand-dot"></span>
      <span class="brand-name">PineHollow Church</span>
    </div>
    <ul class="contact-list">
      <li>
        <svg class="contact-icon" viewBox="0 0 16 16" aria-hidden="true">
          <circle cx="8" cy="8" r="7" fill="none" stroke="var(--brand-blue-bright)" stroke-width="1.6"/>
          <ellipse cx="8" cy="8" rx="3" ry="7" fill="none" stroke="var(--brand-blue-bright)" stroke-width="1.2"/>
          <line x1="1" y1="8" x2="15" y2="8" stroke="var(--brand-blue-bright)" stroke-width="1.2"/>
        </svg>
        ChurchPineHollow.at
      </li>
      <li>
        <svg class="contact-icon" viewBox="0 0 16 16" aria-hidden="true">
          <circle cx="8" cy="8" r="7" fill="none" stroke="var(--brand-blue-bright)" stroke-width="1.6"/>
          <path d="M5.5 4.5 L7 6.5 L6 7.5 Q7 9.5 8.5 10 L9.5 9 L11.5 10.5 L10.5 12 Q6 11.5 4.5 6 Z" fill="var(--brand-blue-bright)"/>
        </svg>
        904-555-0172
      </li>
      <li>
        <svg class="contact-icon" viewBox="0 0 16 16" aria-hidden="true">
          <circle cx="8" cy="8" r="8" fill="var(--brand-blue-bright)"/>
          <rect x="4" y="5.2" width="8" height="5.6" fill="none" stroke="#fff" stroke-width="1"/>
          <path d="M4 5.5 L8 8.5 L12 5.5" fill="none" stroke="#fff" stroke-width="1"/>
        </svg>
        Dwayne@PineHollow.at
      </li>
    </ul>
  </section>

  <section class="card card--front" aria-label="Card front">
    <div class="front-panel">
      <span class="front-dot"></span>
      <span class="front-name">PineHollow<br>Church</span>
    </div>
  </section>

</main>
</body>
</html>
```